Business Card Design

We would like a business card that utilizes our current logo and keeps with the same feel - elegant and organic. Our farm isn't about mass production, it's about excellence, education, beautiful events and flowers - people, culture, and community.

Target Market(s)

Patrons to our farm who are interested in weddings, events, or our flowers and vegetables.

Contact Information for Business Card

Name, address, cell email (Danielle Hoskins, 2716 Wrenfield Rd, Fairhaven, CO 80620, cell 30.412.6638, email danielle@wrenfieldacres.com)

```html
<!DOCTYPE html>
<html lang="en">
<head>
<meta charset="utf-8">
<title>Wrenfield Acres – Business Card</title>
<link rel="stylesheet" href="https://fonts.googleapis.com/css2?family=Goudy+Bookletter+1911&display=swap">
<style>
  :root {
    --backdrop: #d9d7d4;
    --card-stock: #e8e1db;
    --ink: #1b1a19;
    --sage: #718b7c;
    --floral-tone: #d6cdc5;
  }
  html, body {
    margin: 0;
    padding: 0;
    width: 1200px;
    height: 1200px;
    overflow: hidden;
    background: var(--backdrop);
  }
  .canvas {
    position: relative;
    width: 1200px;
    height: 1200px;
  }
  .card {
    position: absolute;
    left: 248px;
    width: 703px;
    height: 400px;
    background: var(--card-stock);
    box-shadow: 0 2px 6px rgba(0,0,0,0.12);
    font-family: "Goudy Bookletter 1911", Georgia, serif;
    color: var(--ink);
  }
  .card--front { top: 176px; }
  .card--back  { top: 650px; }

  .brand-name {
    position: absolute;
    left: 0;
    right: 0;
    top: 168px;
    text-align: center;
    font-size: 44px;
    line-height: 50px;
    letter-spacing: 1px;
    color: var(--sage);
    margin: 0;
    font-weight: 400;
  }

  .holder-name {
    position: absolute;
    left: 34px;
    top: 78px;
    margin: 0;
    font-weight: 400;
    font-size: 37px;
    line-height: 40px;
    letter-spacing: 2.5px;
    text-transform: uppercase;
    white-space: nowrap;
  }

  .contact {
    position: absolute;
    right: 44px;
    top: 264px;
    margin: 0;
    font-style: normal;
    text-align: right;
    font-size: 19px;
    line-height: 28px;
    letter-spacing: 1.4px;
    white-space: nowrap;
  }
  .contact span { display: block; }

  .floral-corner {
    position: absolute;
    left: 0;
    bottom: 0;
    width: 162px;
    height: 200px;
    background: linear-gradient(160deg, var(--floral-tone), var(--card-stock) 85%);
  }
</style>
</head>
<body>
  <main class="canvas">
    <section class="card card--front">
      <h1 class="brand-name">Wrenfield Acres</h1>
    </section>

    <section class="card card--back">
      <h2 class="holder-name">Danielle Hoskins</h2>
      <div class="floral-corner" role="img" aria-label="Line drawing of blossoms and leafy stems in the lower left corner"></div>
      <address class="contact">
        <span>30.412.6638</span>
        <span>danielle@wrenfieldacres.com</span>
        <span>2716 Wrenfield Road</span>
        <span>Fairhaven, CO 80620</span>
      </address>
    </section>
  </main>
</body>
</html>
```